Tidewater Kin - Vehicle Car Wrap - BE BOLD BE CREATIVE - Tell a story about compost

We are Tidewater Kin, a compost community initiative in Miami, FL and our purpose is to leave this planet better that how we found it. Our mission is to create awareness of our undeniable connection with our environment.

Please use the following slogans:
"Revive the earth, embrace compost, join the Dirtopia!"
"Nourishing the earth, one bin at a time"

We offer compost pickup service, and we need a vehicle wrap design that shows and tells a story on the importance of composting for our planet, environment, local farmers and community impact. We are looking for a creative designed. We want people to look at the wrap and understand easily the intention behind our community movement. Composting food scraps is one the best things we can do for our planet and a great way to prevent food waste.
Hint: I love the idea of showing how food scraps from our kitchen nourish our planet's soil to grow wholesome foods. Half wraps are nice too.
Check out IG @tidewaterkinsouth.com
Check out our website www.tidewaterkinsouth.com

Vechicles Kestrel K770 with Ardent body Grand Harbor (see pictures) and Kestrel Porter 480 cargo van

Target Market(s)

Miami Dade County Residents

Industry/Entity Type

Composting - No Food Waste. Our Planet

Font styles to use
Other font styles liked:
• HVD Bodedo and Roboto Slab

Colors
0094D4
00A9DD
6FCCEA
C7EBF8
E9F6FB
00AB8E
00BBA5
67D7C9
C6EFE9
E9F9F6
FFF300
FFF600
FEFA6F
FFFEC7
FFFEE8
E54698
E96AAD
F1A4CE
F9D9EA
FCEFF6

Requirements
Must have
• Impactful and easy to understand. Show how easy it is to compost with us so people can sign up for our program (QR code, steps, process etc)
Nice to have
• Brand Colors (25E5CE) and (F456A6). Pink can have lighter tone
Should not have
• Not branded colors,

```html
<!DOCTYPE html>
<html lang="en">
<head>
<meta charset="utf-8">
<title>Tidewater Kin – Cargo Van Wrap</title>
<link rel="stylesheet" href="https://fonts.googleapis.com/css2?family=Roboto+Slab:wght@400;600;700&display=swap">
<style>
  :root{
    --canvas:#ffffff;
    --wrap-blue:#9fd4e7;
    --wrap-blue-deep:#86c3da;
    --pink:#e54698;
    --pink-deep:#d4328a;
    --pink-soft:#f07ab8;
    --teal:#00bba5;
    --teal-deep:#2f9c94;
    --ink:#1c1c1e;
    --trim:#222326;
    --glass:#3a3d42;
    --tire:#1a1a1a;
    --rim:#b9bcc0;
    --lamp:#c8252d;
    --houses:#8f6f8d;
    --white:#f4f8fa;
  }
  html,body{margin:0;padding:0;width:1200px;height:1200px;overflow:hidden;background:var(--canvas);}
  .van-wrap{display:block;width:1200px;height:1200px;}
  .slab{font-family:'Roboto Slab',serif;}
  .keep-out-label{fill:var(--white);font-size:70px;font-weight:400;}
  .social-handle{fill:var(--pink);font-size:28px;font-weight:600;}
  .web-address{fill:var(--pink);font-size:36px;font-weight:700;}
  .brand-name{fill:var(--ink);font-size:34px;font-weight:700;letter-spacing:1px;}
</style>
</head>
<body>
<svg class="van-wrap" viewBox="0 0 1920 1920" xmlns="http://www.w3.org/2000/svg" aria-label="Tidewater Kin cargo van side wrap">
  <!-- ground shadow -->
  <ellipse class="ground-shadow" cx="960" cy="1300" rx="830" ry="22" fill="#000" opacity="0.18"/>

  <!-- van body -->
  <path class="van-body" d="M190 640 Q195 628 215 628 L1310 640 Q1380 650 1420 700 L1560 880 Q1700 950 1760 1010 L1785 1100 L1785 1160 L1620 1220 L160 1215 L160 1000 Z" fill="var(--wrap-blue)"/>

  <!-- pink rear panel -->
  <path class="rear-panel" d="M190 640 Q195 628 215 628 L740 630 L225 990 L165 1000 Z" fill="var(--pink-deep)"/>
  <g class="rear-stripes" stroke="var(--pink-soft)" stroke-width="14" opacity="0.8">
    <line x1="225" y1="960" x2="495" y2="790"/>
    <line x1="225" y1="990" x2="430" y2="865"/>
    <line x1="250" y1="1000" x2="400" y2="905"/>
  </g>

  <!-- keep out panel -->
  <rect class="keep-out-box" x="215" y="655" width="503" height="107" rx="40" fill="var(--wrap-blue)" stroke="var(--pink)" stroke-width="4"/>
  <rect class="keep-out-mark-frame" x="262" y="668" width="78" height="78" fill="none" stroke="var(--teal-deep)" stroke-width="3"/>
  <g class="keep-out-mark" stroke="var(--pink)" stroke-width="16" stroke-linecap="round">
    <line x1="262" y1="672" x2="335" y2="745"/>
    <line x1="338" y1="668" x2="260" y2="748"/>
  </g>
  <text class="slab keep-out-label" x="380" y="728">keep out</text>

  <!-- accepted scraps icons -->
  <g class="scrap-icons" role="img" aria-label="Small round icons of compostable food scraps" stroke="#d6d6d6" stroke-width="2">
    <circle cx="561" cy="806" r="16" fill="#f0a15a"/><circle cx="605" cy="806" r="16" fill="#f3e6dc"/>
    <circle cx="650" cy="806" r="16" fill="#f2b27a"/><circle cx="696" cy="806" r="16" fill="#f6e6a8"/>
    <circle cx="513" cy="861" r="16" fill="#e6ecb0"/><circle cx="558" cy="861" r="16" fill="#f2d49a"/>
    <circle cx="603" cy="861" r="16" fill="#eed2d2"/><circle cx="649" cy="861" r="16" fill="#ecd8c2"/>
    <circle cx="466" cy="917" r="16" fill="#b88a5a"/><circle cx="511" cy="917" r="16" fill="#d8dcd8"/>
    <circle cx="556" cy="917" r="16" fill="#bfe0e6"/><circle cx="601" cy="917" r="16" fill="#8a5a3a"/>
  </g>

  <!-- sliding door rail -->
  <rect class="door-rail" x="320" y="940" width="420" height="14" rx="6" fill="#6a7880"/>

  <!-- social handle -->
  <rect class="social-mark" x="318" y="976" width="34" height="34" rx="8" fill="none" stroke="var(--pink)" stroke-width="4"/>
  <text class="slab social-handle" x="362" y="1003">@tidewaterkinsouth.com</text>

  <!-- neighbourhood strip -->
  <rect class="neighbourhood" x="222" y="1025" width="513" height="68" fill="var(--houses)" role="img" aria-label="Row of neighbourhood houses"/>

  <!-- panel seams -->
  <g class="panel-seams" stroke="var(--wrap-blue-deep)" stroke-width="3" fill="none">
    <line x1="740" y1="632" x2="745" y2="1200"/>
    <line x1="1155" y1="645" x2="1155" y2="1200"/>
    <path d="M1155 650 L1310 650"/>
  </g>

  <!-- brand badge -->
  <circle class="brand-badge" cx="932" cy="830" r="172" fill="var(--pink)" stroke="var(--ink)" stroke-width="4"/>
  <circle cx="932" cy="830" r="140" fill="var(--wrap-blue)"/>
  <text class="slab brand-name" x="932" y="842" text-anchor="middle">TIDEWATER KIN</text>

  <!-- handles -->
  <rect class="door-handle" x="1070" y="965" width="62" height="12" rx="6" fill="var(--trim)"/>
  <rect class="door-handle" x="1175" y="972" width="62" height="12" rx="6" fill="var(--trim)"/>

  <!-- website -->
  <g class="globe-icon" fill="none" stroke="var(--pink)" stroke-width="4">
    <circle cx="795" cy="1058" r="20"/>
    <ellipse cx="795" cy="1058" rx="8" ry="20"/>
    <line x1="775" y1="1058" x2="815" y2="1058"/>
  </g>
  <text class="slab web-address" x="832" y="1071">www.tidewaterkinsouth.com</text>

  <!-- cab glazing -->
  <path class="side-window" d="M1190 770 Q1192 758 1205 758 L1340 758 Q1380 760 1400 790 L1470 900 L1470 965 L1190 962 Z" fill="var(--glass)"/>
  <line x1="1315" y1="760" x2="1340" y2="962" stroke="#222" stroke-width="6"/>
  <path class="windscreen-edge" d="M1345 748 L1400 760 L1560 895 L1530 900 Z" fill="var(--glass)"/>
  <rect class="mirror" x="1430" y="880" width="40" height="90" rx="12" fill="var(--trim)"/>

  <!-- front lamp -->
  <path class="headlamp" d="M1620 965 L1720 1000 L1735 1040 L1650 1030 Z" fill="var(--glass)"/>
  <path d="M1625 970 L1660 980 L1670 1025 L1650 1028 Z" fill="#f0b429"/>

  <!-- lower trim band -->
  <path class="lower-trim" d="M160 1090 L1785 1090 L1785 1165 L1620 1222 L160 1215 Z" fill="var(--trim)"/>
  <rect class="rocker" x="745" y="1165" width="640" height="32" fill="var(--wrap-blue)"/>
  <rect class="step" x="790" y="1215" width="400" height="16" fill="var(--trim)"/>

  <!-- tail lamp -->
  <path class="tail-lamp" d="M185 920 L222 920 L225 1095 L185 1095 Z" fill="var(--lamp)"/>
  <rect x="185" y="985" width="36" height="70" fill="#e9e9e9"/>

  <!-- wheels -->
  <g class="wheel">
    <circle cx="473" cy="1205" r="102" fill="var(--tire)"/>
    <circle cx="473" cy="1205" r="62" fill="var(--rim)"/>
    <circle cx="473" cy="1205" r="24" fill="#333"/>
  </g>
  <g class="wheel">
    <circle cx="1510" cy="1205" r="102" fill="var(--tire)"/>
    <circle cx="1510" cy="1205" r="62" fill="var(--rim)"/>
    <circle cx="1510" cy="1205" r="24" fill="#333"/>
  </g>
</svg>
</body>
</html>
```